Halvoren Cosmetics Website needs a professional upgrade

I need a new design for an online cosmetics store that looks professional and clean but also has a natural look and feel to it.

The women in the top bar (Image attached) needs to be included and she is on all of our advertising banners/ stands though I would like to come away from the black.

Design Needs:
- 1 x Home Page
- 1 x Products Page

I have plenty more website coming along so hopefully can find someone who I can rely on for a quick turnover :)

Happy designing !

Industry/Entity Type

Store

Number of Pages Required

2 page

Font styles to use
Sans Serif

Requirements
Must have
• - Natural Clean look
Should not have
• - The current black and green colours

```html
<!DOCTYPE html>
<html lang="en">
<head>
<meta charset="utf-8">
<title>Halvoren Cosmetics – Home</title>
<link rel="stylesheet" href="https://fonts.googleapis.com/css2?family=Roboto:wght@400;500;700&family=Ubuntu:wght@400;500&family=Oswald:wght@400;500&display=swap">
<style>
:root{
  --pink:#d9546f;
  --pink-soft:#e57a8f;
  --pink-deep:#c9415d;
  --brown:#6b4e39;
  --brown-dark:#5a412f;
  --text:#444;
  --muted:#777;
  --line:#d8d8d8;
  --white:#fff;
  --green-soft:#cfe3c4;
}
*{box-sizing:border-box;margin:0;padding:0}
html,body{width:1200px;height:3087px;overflow:hidden}
body{position:relative;background:var(--white);font-family:"Roboto",sans-serif;color:var(--text)}
.abs{position:absolute}
a{color:inherit;text-decoration:none}

/* header */
.follow-label{left:134px;top:26px;font-size:17px;font-weight:500;color:#333}
.social{left:103px;top:64px;display:flex;gap:10px}
.social span{width:36px;height:36px;border:2px solid #333;border-radius:50%}
.contact-top{left:880px;font-size:18px;color:#333;display:flex;align-items:center;gap:10px}
.contact-top b{font-weight:400;color:var(--pink)}
.contact-top svg{flex:none}
.phone-line{top:31px}.fax-line{top:76px}
.brand-dome{left:495px;top:110px;width:210px;height:100px;border-radius:0 0 105px 105px;background:var(--white);z-index:3}
.brand{left:500px;top:8px;width:200px;text-align:center;z-index:4}
.brand-mark{width:68px;height:68px;border-radius:50%;background:var(--brown);margin:0 auto 8px}
.brand-name{font-family:"Ubuntu",sans-serif;font-size:24px;font-weight:400;color:var(--brown);line-height:1.2;letter-spacing:1px}

/* nav */
.main-nav{left:0;top:138px;width:1200px;height:62px;background:var(--pink);z-index:2}
.main-nav a{position:absolute;top:20px;font-size:15px;color:var(--white)}

/* hero */
.hero{left:0;top:200px;width:1200px;height:540px;overflow:hidden}
.hero-photo{position:absolute;inset:0;background:linear-gradient(100deg,#cfe2c8 0%,#e4efdc 35%,#eef3e8 55%,#efd9c8 72%,#e9cdb9 85%,#d8c3b4 100%)}
.hero-title{position:absolute;left:99px;top:94px;font-family:"Ubuntu",sans-serif;font-size:42px;font-weight:500;color:var(--pink);text-shadow:0 0 6px rgba(255,255,255,.8)}
.hero-sub{position:absolute;left:103px;top:178px;padding:6px 10px;background:rgba(255,255,255,.35);font-family:"Ubuntu",sans-serif;font-size:35px;color:var(--white)}
.btn-primary{position:absolute;background:var(--pink);color:var(--white);font-size:16px;font-weight:500;display:flex;align-items:center;justify-content:center;border-radius:3px}
.hero .btn-primary{left:99px;top:277px;width:123px;height:46px;border:2px solid var(--white)}
.hero-dots{position:absolute;left:99px;top:360px;display:flex;gap:4px}
.hero-dots span{width:12px;height:12px;border-radius:50%;background:#a9a9a9}
.hero-dots span:first-child{background:var(--pink)}
.hero-wave{position:absolute;left:0;bottom:0}

/* welcome */
.section-title{font-family:"Ubuntu",sans-serif;font-size:33px;font-weight:500;color:var(--pink);text-align:center;width:1200px;left:0}
.welcome-title{top:802px}
.ornament{left:520px;top:862px}
.welcome-copy{left:144px;top:910px;width:912px;text-align:center;font-size:13.5px;line-height:26px;color:#555}

.carousel-arrow{top:1155px}
.info-card{width:210px;text-align:center}
.info-card .icon{position:absolute;left:56px;top:0;width:98px;height:98px;border-radius:50%;border:4px solid var(--white);z-index:2}
.info-card .disc{position:absolute;left:2px;top:60px;width:206px;height:206px;border-radius:50%;color:var(--white)}
.info-card .disc::after{content:"";position:absolute;inset:8px;border:2px dashed rgba(255,255,255,.7);border-radius:50%}
.info-card h3{margin-top:62px;font-family:"Ubuntu",sans-serif;font-size:19px;font-weight:500}
.info-card p{margin:8px auto 0;width:150px;font-size:13px;line-height:19px}
.is-pink{background:var(--pink-soft)}
.is-brown{background:var(--brown)}

.divider{left:99px;top:1368px;width:1002px;height:2px;background:var(--line)}

/* products */
.featured-title{top:1406px}
.circle-arrow{top:1410px}
.product{width:241px;text-align:center}
.product-shot{width:241px;height:228px;background:linear-gradient(#fff,#f3f3f3);border:8px solid #f1f1f1;box-shadow:0 0 6px rgba(0,0,0,.08)}
.product-shot div{width:150px;height:150px;margin:30px auto 0;background:linear-gradient(160deg,#eaeaea,#cfcfcf);border-radius:8px}
.stars{margin-top:20px;color:var(--pink);font-size:13px;letter-spacing:2px}
.product h4{margin-top:8px;font-size:17px;font-weight:400;color:#222}
.buy{margin-top:20px;display:flex;justify-content:space-between;align-items:center;padding:0 16px 0 16px}
.price{font-size:19px;color:#222}
.price.is-active{color:var(--pink)}
.add-cart{width:119px;height:37px;border:2px solid #333;font-size:13px;font-weight:500;display:flex;align-items:center;justify-content:center;color:#222}
.add-cart.is-active{background:var(--pink);border-color:var(--pink);color:var(--white)}

/* treatments */
.treatments{left:0;top:1910px;width:1200px;height:354px;background:linear-gradient(180deg,#d95a73,#d14f6b)}
.treatments h2{position:absolute;top:30px;width:1200px;text-align:center;font-family:"Ubuntu",sans-serif;font-size:29px;font-weight:500;color:var(--white)}
.treatment{position:absolute;top:118px;color:var(--white)}
.treatment-photo{position:absolute;left:0;top:0;width:180px;height:180px;border-radius:50%;border:6px solid var(--white);background:radial-gradient(circle at 45% 55%,#8cc468,#e9efe2 70%)}
.treatment-body{position:absolute;left:214px;top:20px;width:250px}
.treatment-body h3{font-family:"Ubuntu",sans-serif;font-size:23px;font-weight:400}
.treatment-body p{margin-top:8px;font-size:14px;line-height:21px;text-align:justify}
.treatment-body a{display:block;margin-top:6px;font-size:15px;font-weight:700}

/* sale */
.sale{left:0;top:2284px;width:1200px;height:380px;background:linear-gradient(180deg,#fafafa,#f1f1f1)}
.sale-head{position:absolute;left:0;top:36px;width:684px;text-align:center;font-family:"Oswald",sans-serif;font-size:29px;color:#333}
.sale-ship{position:absolute;left:177px;top:77px;width:329px;height:63px;background:var(--brown);color:var(--white);font-family:"Oswald",sans-serif;font-size:36px;display:flex;align-items:center;justify-content:center}
.sale-lead{position:absolute;left:0;top:160px;width:684px;text-align:center;font-size:20px;color:#222}
.sale-copy{position:absolute;left:212px;top:200px;width:260px;text-align:center;font-size:13px;line-height:22px;color:#444}
.btn-outline{position:absolute;left:282px;top:262px;width:123px;height:43px;border:2px solid #555;font-size:14px;display:flex;align-items:center;justify-content:center;color:#222}
.sale-photo{position:absolute;left:638px;top:30px;width:525px;height:240px;border-radius:6px;background:linear-gradient(120deg,#f4f6ef 0%,#bfe08a 30%,#79b63f 55%,#3c3f3b 80%,#f1f1f1 100%)}

/* footer */
.footer-wave{left:0;top:2600px}
.site-footer{left:0;top:2700px;width:1200px;height:387px;background:var(--brown);color:var(--white)}
.footer-brand{position:absolute;left:99px;top:98px;width:200px;text-align:center}
.footer-brand .brand-mark{background:transparent;border:3px solid var(--white);width:80px;height:80px}
.footer-brand .brand-name{color:var(--white);font-size:26px}
.footer-col{position:absolute;top:56px}
.footer-col h5{font-size:16px;font-weight:500;letter-spacing:.5px;margin-bottom:24px}
.links li{list-style:none;font-size:14px;margin-bottom:13px}
.links li::before{content:"> ";}
.contact-row{display:flex;gap:16px;margin-bottom:20px;font-size:12.5px;line-height:18px}
.contact-row svg{flex:none}
.contact-row b{font-weight:500;display:block}
.form-row{display:flex;gap:14px;margin-bottom:14px}
.field{height:36px;border:1.5px solid rgba(255,255,255,.8);font-size:10px;padding:8px 10px}
.field.half{width:138px}
.field.full{width:286px;height:64px}
.send{width:118px;height:36px;border:1.5px solid var(--white);font-size:11px;display:flex;align-items:center;justify-content:center}
.footer-rule{position:absolute;left:99px;top:321px;width:1002px;height:1px;background:rgba(255,255,255,.5)}
.copyright{position:absolute;left:99px;top:348px;font-size:14px}
.footer-social{position:absolute;left:912px;top:340px;display:flex;gap:8px}
.footer-social span{width:32px;height:32px;border:2px solid var(--white);border-radius:50%}
</style>
</head>
<body>

<header>
  <div class="abs follow-label">FOLLOW US:</div>
  <div class="abs social" aria-label="Social links"><span></span><span></span><span></span><span></span></div>

  <div class="abs brand-dome"></div>
  <div class="abs brand">
    <div class="brand-mark"></div>
    <div class="brand-name">HALVOREN COSMETICS</div>
  </div>

  <div class="abs contact-top phone-line">
    <svg width="34" height="34" viewBox="0 0 34 34"><circle cx="17" cy="17" r="15" fill="none" stroke="#d9546f" stroke-width="2"/><path d="M12 10l3 0 1.5 4-2 1.5a9 9 0 0 0 4 4l1.5-2 4 1.5v3a2 2 0 0 1-2 2A13 13 0 0 1 10 12a2 2 0 0 1 2-2z" fill="#d9546f"/></svg>
    <span>Phone: <b>02 5550 1842</b></span>
  </div>
  <div class="abs contact-top fax-line">
    <svg width="34" height="34" viewBox="0 0 34 34"><circle cx="17" cy="17" r="15" fill="none" stroke="#d9546f" stroke-width="2"/><rect x="11" y="9" width="12" height="6" fill="none" stroke="#d9546f" stroke-width="2"/><rect x="9" y="15" width="16" height="9" rx="1" fill="#d9546f"/><rect x="12" y="21" width="10" height="5" fill="#fff" stroke="#d9546f" stroke-width="1.5"/></svg>
    <span>Fax: <b>02 5550 1843</b></span>
  </div>
</header>

<nav class="abs main-nav">
  <a style="left:99px">Home</a>
  <a style="left:185px">About Us</a>
  <a style="left:294px">Products</a>
  <a style="left:403px">About Aloe</a>
  <a style="left:712px">Treatments</a>
  <a style="left:827px">Media</a>
  <a style="left:906px">Success Stories</a>
  <a style="left:1045px">Contact</a>
</nav>

<section class="abs hero">
  <div class="hero-photo" role="img" aria-label="Woman touching her cheek in front of sliced aloe leaves"></div>
  <h1 class="hero-title">Natural Skin Care Specialists</h1>
  <div class="hero-sub">Halvoren Cosmetics</div>
  <a class="btn-primary">Read More</a>
  <div class="hero-dots"><span></span><span></span><span></span><span></span><span></span></div>
  <svg class="hero-wave" width="1200" height="110" viewBox="0 0 1200 110">
    <path d="M0 60 C300 110 700 110 1200 10 L1200 110 L0 110Z" fill="#d9546f"/>
    <path d="M0 66 C300 118 720 118 1200 40 L1200 110 L0 110Z" fill="#fff"/>
  </svg>
</section>

<h2 class="abs section-title welcome-title">Welcome to Halvoren Cosmetics</h2>
<svg class="abs ornament" width="160" height="30" viewBox="0 0 160 30">
  <line x1="0" y1="15" x2="62" y2="15" stroke="#d9546f" stroke-width="1.5"/>
  <line x1="98" y1="15" x2="160" y2="15" stroke="#d9546f" stroke-width="1.5"/>
  <circle cx="80" cy="15" r="13" fill="none" stroke="#d9546f" stroke-width="1.5"/>
  <circle cx="80" cy="15" r="7" fill="#d9546f"/>
</svg>
<p class="abs welcome-copy">Halvoren Cosmetics produces a range of premium natural skincare products based on the healing and soothing Aloe Vera plant to assist people with eczema, psoriasis, dermatitis, acne, pigmentation and those looking for effective natural skincare and daily tonic. We are 100% Australian made and owned and all our products have been tried and tested on friends and family – in fact that's how we started.</p>

<svg class="abs carousel-arrow" style="left:36px" width="24" height="46" viewBox="0 0 24 46"><path d="M22 2 L3 23 L22 44" fill="none" stroke="#444" stroke-width="2"/></svg>
<svg class="abs carousel-arrow" style="left:1140px" width="24" height="46" viewBox="0 0 24 46"><path d="M2 2 L21 23 L2 44" fill="none" stroke="#444" stroke-width="2"/></svg>

<article class="abs info-card" style="left:97px;top:1026px">
  <div class="icon is-brown" role="img" aria-label="Aloe plant icon"></div>
  <div class="disc is-pink"><h3>Eczema Treatments</h3><p>Eczema, is a skin irritation characterized by red, flaky skin, sometimes with cracks</p></div>
</article>
<article class="abs info-card" style="left:344px;top:1026px">
  <div class="icon is-pink" role="img" aria-label="Head profile icon"></div>
  <div class="disc is-brown"><h3>Acne Treatments</h3><p>Acne is a skin condition caused by changes in the skin structures consisting of hair follicle.</p></div>
</article>
<article class="abs info-card" style="left:591px;top:1026px">
  <div class="icon is-brown" role="img" aria-label="Aloe leaves icon"></div>
  <div class="disc is-pink"><h3>Bowel Syndrome</h3><p>IBS is a functional bowel disorder of the gastrointestinal tract characterized by recurrent</p></div>
</article>
<article class="abs info-card" style="left:838px;top:1026px">
  <div class="icon is-pink" role="img" aria-label="Cream tube icon"></div>
  <div class="disc is-brown"><h3>Ingredients Glossary</h3><p>The extract of the Aloe Bar badensis Miller plant is renowned for its unique soothing</p></div>
</article>

<div class="abs divider"></div>

<h2 class="abs section-title featured-title">Featured Products</h2>
<svg class="abs circle-arrow" style="left:415px" width="30" height="30" viewBox="0 0 30 30"><circle cx="15" cy="15" r="13" fill="none" stroke="#333" stroke-width="2"/><path d="M17 9 L11 15 L17 21" fill="none" stroke="#333" stroke-width="2"/></svg>
<svg class="abs circle-arrow" style="left:761px" width="30" height="30" viewBox="0 0 30 30"><circle cx="15" cy="15" r="13" fill="none" stroke="#333" stroke-width="2"/><path d="M13 9 L19 15 L13 21" fill="none" stroke="#333" stroke-width="2"/></svg>

<article class="abs product" style="left:99px;top:1490px">
  <div class="product-shot"><div role="img" aria-label="Jar of silk moisturiser with purple box"></div></div>
  <div class="stars">★★★★☆</div>
  <h4>Silk Moisturiser</h4>
  <div class="buy"><span class="price is-active">$650.00</span><a class="add-cart is-active">ADD TO CART</a></div>
</article>
<article class="abs product" style="left:353px;top:1490px">
  <div class="product-shot"><div role="img" aria-label="Boxed aloe vera soap bar"></div></div>
  <div class="stars">★★★★☆</div>
  <h4>Aloe Vera Soap</h4>
  <div class="buy"><span class="price">$650.00</span><a class="add-cart">ADD TO CART</a></div>
</article>
<article class="abs product" style="left:607px;top:1490px">
  <div class="product-shot"><div role="img" aria-label="Tube of pigmentation control balm with box"></div></div>
  <div class="stars">★★★★☆</div>
  <h4>Pigmentation Control Balm</h4>
  <div class="buy"><span class="price">$650.00</span><a class="add-cart">ADD TO CART</a></div>
</article>
<article class="abs product" style="left:860px;top:1490px">
  <div class="product-shot"><div role="img" aria-label="After sun treatment pack with tube and jar"></div></div>
  <div class="stars">★★★★☆</div>
  <h4>After Sun Treatment Pack</h4>
  <div class="buy"><span class="price">$650.00</span><a class="add-cart">ADD TO CART</a></div>
</article>

<section class="abs treatments">
  <h2>Our Treatments</h2>
  <div class="treatment" style="left:99px">
    <div class="treatment-photo" role="img" aria-label="Cut aloe leaf pieces"></div>
    <div class="treatment-body">
      <h3>After Sun Care</h3>
      <p>Sunburn occurs when exposure to UV light exceeds the protective capacity of an individual's melanin.</p>
      <a>Read More ➔</a>
    </div>
  </div>
  <div class="treatment" style="left:620px">
    <div class="treatment-photo" role="img" aria-label="Aloe plant beside a jar of cream"></div>
    <div class="treatment-body">
      <h3>Eczema &amp; Psoriasis</h3>
      <p>Eczema, is a skin irritation characterized by red, flaky skin, sometimes with cracks or tiny blisters.</p>
      <a>Read More ➔</a>
    </div>
  </div>
</section>

<section class="abs sale">
  <div class="sale-head">SALE UP TO 50% OFF</div>
  <div class="sale-ship">$8 SHIPPING AUS</div>
  <div class="sale-lead">Digestive enzyme deficiency and intestinal dysbiosis</div>
  <p class="sale-copy">Our products can be used by the whole family and because we don't use any parabens, mineral oils, propylene glycol.</p>
  <a class="btn-outline">SHOP NOW</a>
  <div class="sale-photo" role="img" aria-label="Glass bottle of aloe gel with cut aloe leaves on a slate board"></div>
</section>

<svg class="abs footer-wave" width="1200" height="110" viewBox="0 0 1200 110">
  <path d="M0 30 C320 110 760 110 1200 30 L1200 50 C760 122 320 122 0 58Z" fill="#d9546f"/>
  <path d="M0 72 C320 130 760 126 1200 62 L1200 110 L0 110Z" fill="#6b4e39"/>
</svg>

<footer class="abs site-footer">
  <div class="footer-brand">
    <div class="brand-mark"></div>
    <div class="brand-name">HALVOREN COSMETICS</div>
  </div>

  <div class="footer-col" style="left:360px">
    <h5>USEFULL LINKS</h5>
    <ul class="links">
      <li>Home</li><li>About Us</li><li>Products</li><li>About Aloe</li><li>Treatments</li><li>Contact Us</li>
    </ul>
  </div>

  <div class="footer-col" style="left:535px;width:250px">
    <h5>CONTACT US</h5>
    <div class="contact-row">
      <svg width="34" height="34" viewBox="0 0 34 34"><circle cx="17" cy="17" r="15" fill="none" stroke="#fff" stroke-width="1.5"/><path d="M17 9a5 5 0 0 1 5 5c0 4-5 10-5 10s-5-6-5-10a5 5 0 0 1 5-5z" fill="#fff"/><circle cx="17" cy="14" r="2" fill="#6b4e39"/></svg>
      <div><b>HALVOREN COSMETICS,</b>ABN 41 208 913 775 Unit 7/14 Harbour Lane, Marlow NSW</div>
    </div>
    <div class="contact-row">
      <svg width="34" height="34" viewBox="0 0 34 34"><circle cx="17" cy="17" r="15" fill="none" stroke="#fff" stroke-width="1.5"/><rect x="13" y="9" width="8" height="16" rx="1.5" fill="none" stroke="#fff" stroke-width="1.5"/></svg>
      <div><b>PHONE NUMBER:</b>02 5550 1842</div>
    </div>
    <div class="contact-row">
      <svg width="34" height="34" viewBox="0 0 34 34"><circle cx="17" cy="17" r="15" fill="none" stroke="#fff" stroke-width="1.5"/><rect x="10" y="12" width="14" height="10" fill="#fff"/><path d="M10 12 L17 18 L24 12" fill="none" stroke="#6b4e39" stroke-width="1.5"/></svg>
      <div><b>EMAIL:</b>sales@halvorencosmetics.example</div>
    </div>
  </div>

  <div class="footer-col" style="left:815px">
    <h5>CONTACT FORM</h5>
    <div class="form-row"><div class="field half">Name</div><div class="field half">Phone</div></div>
    <div class="form-row"><div class="field full">Message</div></div>
    <div class="send">SEND MESSAGE</div>
  </div>

  <div class="footer-rule"></div>
  <p class="copyright">© 2016 Halvoren Cosmetics. All Rights Reserved.</p>
  <div class="footer-social"><span></span><span></span><span></span><span></span><span></span></div>
</footer>

</body>
</html>
```